Coffee distributor in London website concept design

We have just launched a rebranded coffee distributor in London supplying coffee to bars, restaurants, coffee shops and hotels.

We sell coffee, coffee machines, barista training and work with 2 brands - Tavolieri and Vardo. We want the site to have calls to action (i.e. advertising boxes that promote something such as a new blend or machine.

The site should be focused towards foodservice clients such as those mentioned above, and should follow the colours of the logo (the current site is www.brunotaza42.com). There should be around 200 - 250 words on the home page, and should make us look professional, modern, knowledgeable and most importantly, unique.

Sites to look at:
http://www.quillharbor.com/
http://www.pellamarsh.com/
http://www.redkettlebeans.com/
http://www.tobiasfernley.com/
http://www.vellicauk.com/
http://www.harvestbrewed.com/
http://www.quartzbean.co.uk/
http://www.trebbiabean.co.uk/
http://www.tavolieri.it/en/
http://www.vardo.co.uk/
Updates

Just a quick reminder, we are a coffee distributor/wholesaler, not a coffee shop.

Some sites to look Sites to look at:
http://www.vellicauk.com/
http://www.vardo.co.uk/at:

Target Market(s)

We are targeting businesses, and will be using SEO and social media to be found. Our target customers are restaurants, coffee shops, hotels, pubs and bars.

Industry/Entity Type

Advertising

Font styles to use
Sans Serif

Colors
ec1f27

Requirements
Must have
• The home page, and maybe inner pages to a lesser extent, should have a banner which changes, and some advertising boxes (look at http://www.tobiasfernley.com for example).

There should also be a minimum of 200 words on a page.

We currently have a Facebook page, but will be looking to launch Instagram, twitter, YouTube and Google+, so there should be icons (ideally branded in our colour scheme and look) which link to these pages.

```html
<!DOCTYPE html>
<html lang="en">
<head>
<meta charset="utf-8">
<title>Bruno Taza 42 — Coffee Distributor</title>
<link href="https://fonts.googleapis.com/css2?family=Bebas+Neue&family=Montserrat:wght@700;800&family=Raleway:wght@300;400;600&display=swap" rel="stylesheet">
<style>
  :root {
    --brand-red: #d91920;
    --brand-red-deep: #b80f16;
    --white: #ffffff;
    --ink: #555555;
    --ink-soft: #7a7a7a;
    --night: #0b0b0b;
    --charcoal: #1a1a1a;
    --espresso: #3a1e10;
    --crema: #c98a4a;
    --line: #e2e2e2;
  }
  * { margin: 0; padding: 0; box-sizing: border-box; }
  html, body { width: 819px; height: 1200px; overflow: hidden; }
  body { position: relative; background: var(--brand-red); font-family: "Raleway", sans-serif; color: var(--ink); }
  .abs { position: absolute; }

  /* Header */
  .site-header { left: 0; top: 0; width: 819px; height: 86px; background: var(--brand-red); z-index: 5; }
  .brand-badge { left: 124px; top: -40px; width: 160px; height: 160px; border-radius: 50%; background: var(--white); border: 5px solid var(--brand-red-deep); z-index: 6; display: flex; align-items: flex-end; justify-content: center; padding-bottom: 44px; }
  .brand-name { font-family: "Bebas Neue", sans-serif; font-size: 30px; color: var(--brand-red-deep); line-height: 1; white-space: nowrap; }
  .social-links { left: 646px; top: 17px; display: flex; gap: 1px; z-index: 6; }
  .social-links span { width: 26px; height: 26px; border-radius: 50%; background: var(--white); border: 3px solid #8a1015; display: block; }
  .main-nav { right: 29px; top: 52px; display: flex; gap: 12px; z-index: 6; }
  .main-nav a, .footer-nav a { font-family: "Bebas Neue", sans-serif; color: var(--white); text-decoration: none; letter-spacing: .2px; }
  .main-nav a { font-size: 20px; }

  /* Hero */
  .hero { left: 0; top: 86px; width: 819px; height: 284px; background: radial-gradient(ellipse at 28% 40%, #c98a4a 0%, #7a4220 35%, #2a150a 75%, #140a05 100%); }
  .slide-arrow { top: 194px; width: 68px; height: 68px; border-radius: 50%; background: var(--white); z-index: 3; }
  .slide-arrow.prev { left: -32px; }
  .slide-arrow.next { right: -32px; }
  .slide-arrow svg { position: absolute; top: 25px; }
  .slide-arrow.prev svg { right: 14px; }
  .slide-arrow.next svg { left: 14px; }
  .slide-dots { left: 383px; top: 311px; display: flex; gap: 3px; z-index: 3; }
  .slide-dots span { width: 11px; height: 11px; border-radius: 50%; background: var(--brand-red); }
  .slide-dots span.active { background: var(--night); }

  /* Welcome panel */
  .welcome-panel { left: 110px; top: 324px; width: 600px; height: 522px; background: var(--white); box-shadow: 0 0 6px rgba(255,220,120,.6); z-index: 2; }
  .welcome-panel .panel-top { position: absolute; left: 0; top: 0; width: 600px; height: 46px; background: rgba(255,255,255,.82); }
  .welcome-title { position: absolute; left: 0; width: 600px; top: 12px; text-align: center; font-family: "Bebas Neue", sans-serif; font-size: 31px; color: var(--brand-red); }
  .welcome-copy { position: absolute; left: 12px; top: 58px; width: 258px; }
  .lead { font-size: 10.5px; color: var(--brand-red); line-height: 1.05; margin-bottom: 14px; }
  .welcome-copy p.body { font-size: 7.4px; line-height: 1.46; text-align: justify; color: var(--ink); margin-bottom: 10px; }
  .welcome-photo { position: absolute; left: 284px; top: 54px; width: 303px; height: 200px; background: radial-gradient(ellipse at 55% 35%, #c9a07a 0%, #6a3f22 40%, #1a0d06 85%); }

  .feature-card { top: 288px; width: 156px; height: 228px; border: 1px solid var(--line); background: var(--white); position: absolute; }
  .feature-card h3 { font-family: "Montserrat", sans-serif; font-weight: 800; font-size: 19px; color: var(--brand-red); text-align: center; margin-top: 4px; letter-spacing: .2px; }
  .feature-card .card-photo { width: 134px; height: 134px; border-radius: 50%; border: 4px solid var(--brand-red); margin: 4px auto 0; }
  .card-photo.beans { background: radial-gradient(circle at 40% 45%, #f2f2f2 0%, #c9c2b8 28%, #5a3520 55%, #2a150a 100%); }
  .card-photo.pour { background: radial-gradient(circle at 40% 60%, #eeeeee 0%, #b8ada0 25%, #4a2a16 55%, #1e0f06 100%); }
  .card-photo.bokeh { background: radial-gradient(circle at 50% 65%, #f0e6dc 0%, #d04040 25%, #8a1212 65%, #3a0606 100%); }
  .feature-card p { font-size: 7.4px; line-height: 1.45; text-align: justify; color: var(--ink); padding: 10px 4px 0 5px; }
  .read-more { font-size: 8px; color: var(--brand-red); padding: 4px 0 0 5px; display: flex; align-items: center; gap: 4px; }

  /* Coffee first */
  .coffee-first { left: 0; top: 852px; width: 819px; text-align: center; color: var(--white); }
  .coffee-first h2 { font-family: "Montserrat", sans-serif; font-weight: 800; font-size: 21px; letter-spacing: .2px; line-height: 1.1; }
  .coffee-first .tagline { font-size: 14px; font-weight: 300; color: #f3b0b0; line-height: 1.1; }
  .coffee-first .story { width: 480px; margin: 9px auto 0; font-size: 7.8px; line-height: 1.38; }
  .coffee-first .cta { font-family: "Montserrat", sans-serif; font-weight: 700; font-size: 7.5px; margin-top: 7px; display: inline-flex; align-items: center; gap: 5px; }

  /* Newsletter band */
  .brew-band { left: 0; top: 965px; width: 819px; height: 113px; background: var(--charcoal); }
  .brew-band .band-photo { position: absolute; left: 0; top: 0; width: 196px; height: 113px; clip-path: polygon(0 0, 148px 0, 196px 113px, 0 113px); background: linear-gradient(100deg, #c98a4a 0%, #6a4025 45%, #2a170b 100%); }
  .brew-band .notch { position: absolute; left: 403px; top: 0; }
  .band-heading { position: absolute; top: 17px; font-family: "Bebas Neue", sans-serif; font-size: 25px; color: var(--white); text-align: center; }
  .band-sub { position: absolute; top: 49px; font-size: 8px; color: #8a8a8a; text-align: center; }
  .newsletter-form { position: absolute; left: 254px; top: 78px; display: flex; }
  .newsletter-form .field { width: 264px; height: 31px; background: var(--white); font-size: 8px; color: #333; padding: 10px 9px; }
  .newsletter-form .go { width: 75px; height: 31px; background: var(--brand-red); color: var(--white); font-family: "Montserrat", sans-serif; font-weight: 700; font-size: 11px; display: flex; align-items: center; justify-content: center; }

  /* Footer */
  .site-footer { left: 0; top: 1078px; width: 819px; height: 122px; background: var(--night); }
  .footer-brand { position: absolute; left: 160px; top: 42px; font-family: "Bebas Neue", sans-serif; font-size: 30px; color: #3a3a3a; }
  .footer-nav { position: absolute; left: 310px; top: 22px; display: flex; gap: 13px; }
  .footer-nav a { font-size: 17px; }
  .copyright { position: absolute; left: 313px; top: 53px; font-family: "Bebas Neue", sans-serif; font-size: 11px; color: #444; }
</style>
</head>
<body>

<header class="site-header abs">
  <nav class="main-nav abs">
    <a href="#">Verieties</a><a href="#">Happenings</a><a href="#">Where to find</a><a href="#">Story</a><a href="#">Reciepes</a><a href="#">Contact</a>
  </nav>
  <div class="social-links abs" aria-label="Social links"><span></span><span></span><span></span><span></span></div>
</header>
<div class="brand-badge abs"><span class="brand-name">Bruno Taza 42</span></div>

<section class="hero abs" role="img" aria-label="Banner photo of a cup of tea and a teapot on a warm table with coffee beans"></section>
<div class="slide-arrow prev abs"><svg width="16" height="18" viewBox="0 0 16 18"><path d="M16 0 L0 9 L16 18 Z" fill="#d91920"/></svg></div>
<div class="slide-arrow next abs"><svg width="16" height="18" viewBox="0 0 16 18"><path d="M0 0 L16 9 L0 18 Z" fill="#d91920"/></svg></div>
<div class="slide-dots abs"><span class="active"></span><span></span><span></span><span></span></div>

<main class="welcome-panel abs">
  <div class="panel-top"></div>
  <h1 class="welcome-title">Welcome</h1>
  <div class="welcome-copy">
    <p class="lead">Sed ut perspiciatis unde omnis iste natus error sit voluptatem accusantium doloremque laudantium.</p>
    <p class="body">totam rem aperiam, eaque ipsa quae ab illo inventore veritatis et quasi architecto beatae vitae dicta sunt explicabo. Nemo enim ipsam voluptatem quia voluptas sit aspernatur aut odit aut fugit, sed quia consequuntur magni dolores eos qui ratione voluptatem sequi nesciunt. Neque porro quisquam est, qui dolorem ipsum quia dolor sit amet, consectetur, adipisci velit, sed quia non numquam eius modi tempora incidunt ut labore et dolore</p>
    <p class="body">Sed ut perspiciatis unde omnis iste natus error sit voluptatem accusantium doloremque laudantium, totam rem aperiam, eaque ipsa quae ab illo inventore veritatis et quasi architecto beatae vitae dicta sunt explicabo. Nemo enim ipsam voluptatem quia voluptas sit aspernatur aut odit aut fugit, sed quia consequuntur magni dolores eos qui ratione voluptatem sequi nesciunt. Neque porro quisquam est, qui dolorem ipsum quia dolor sit amet, consectetur.</p>
  </div>
  <div class="welcome-photo" role="img" aria-label="Photo of a steaming cup of coffee beside a scoop of roasted beans"></div>

  <article class="feature-card" style="left:56px">
    <h3>VERIETIES</h3>
    <div class="card-photo beans" role="img" aria-label="Photo of a white cup of coffee on a bed of beans"></div>
    <p>totam rem aperiam, eaque ipsa quae ab illo inventore veritatis et quasi architecto.......</p>
    <div class="read-more">read more <svg width="5" height="6" viewBox="0 0 5 6"><path d="M0 0 L5 3 L0 6 Z" fill="#111"/></svg></div>
  </article>
  <article class="feature-card" style="left:223px">
    <h3>RECIEPES</h3>
    <div class="card-photo pour" role="img" aria-label="Photo of coffee being poured into a cup over beans"></div>
    <p>totam rem aperiam, eaque ipsa quae ab illo inventore veritatis et quasi architecto.......</p>
    <div class="read-more">read more <svg width="5" height="6" viewBox="0 0 5 6"><path d="M0 0 L5 3 L0 6 Z" fill="#111"/></svg></div>
  </article>
  <article class="feature-card" style="left:388px">
    <h3>STORIES</h3>
    <div class="card-photo bokeh" role="img" aria-label="Photo of a small cup and milk jug against red festive lights"></div>
    <p>totam rem aperiam, eaque ipsa quae ab illo inventore veritatis et quasi architecto.......</p>
    <div class="read-more">read more <svg width="5" height="6" viewBox="0 0 5 6"><path d="M0 0 L5 3 L0 6 Z" fill="#111"/></svg></div>
  </article>
</main>

<section class="coffee-first abs">
  <h2>FOR THOSE WHO PUT COFFEE FIRST</h2>
  <p class="tagline">If you love great coffee, then rest assured we love you right back.</p>
  <p class="story">Coffee lovers like you have kept the fire burning in us for over 150 years. That passion comes through in every bag (whole bean or ground) and every Brewnest® B-Pod® pack of Quill Harbor Coffee. Always crafted from 100% Arabica coffee beans under the expert care of master roasters -- just the way you love it.</p>
  <span class="cta">READ MORE <svg width="6" height="9" viewBox="0 0 6 9"><path d="M0 0 L6 4.5 L0 9 Z" fill="#111"/></svg></span>
</section>

<section class="brew-band abs">
  <div class="band-photo" role="img" aria-label="Photo of coffee cups and a grinder on a table of beans"></div>
  <svg class="notch" width="14" height="10" viewBox="0 0 14 10"><path d="M0 0 L14 0 L7 10 Z" fill="#d91920"/></svg>
  <h2 class="band-heading" style="left:206px;width:200px">SEE WHAT'S BREWING</h2>
  <p class="band-sub" style="left:206px;width:200px">Join the coffee talk.</p>
  <h2 class="band-heading" style="left:417px;width:200px">NEWS LETTER</h2>
  <p class="band-sub" style="left:397px;width:240px">Enter your e-mail for the latest from Bruno Taza</p>
  <div class="newsletter-form"><div class="field">subscribe our newsletter</div><div class="go">GO</div></div>
</section>

<footer class="site-footer abs">
  <span class="footer-brand">Bruno Taza 42</span>
  <nav class="footer-nav">
    <a href="#">Verieties</a><a href="#">Happenings</a><a href="#">Where to find</a><a href="#">Story</a><a href="#">Reciepes</a><a href="#">Contact</a>
  </nav>
  <p class="copyright">© 2013 BRUNO TAZA 42. ALL RIGHT RESERVE</p>
</footer>

</body>
</html>
```